Etikett für für Teigtaschen mit Käsefüllung
Zielgruppe
Ich bin Kleinunternehmerin und stelle Teigtaschen her.
Meine Zielgruppe sind Feinkostläden bzw. Endverbraucher
Aufgabenstellung
Ich übersende Ihnen erstmals eine Vorlage der Etikette für Teigtaschen mit Käsefülle.... je nach Fülle, sollte ein tolles Bild für die jeweilige Fülle - in diesem Fall 'Käse' erscheinen. Es sind ja mehrere Käsesorten in der Teigtasche enthalten. Meine LOGO-Daten sind bei Ihnen gespeichert.
Bei der Nährwerttabelle ändern sich noch die Angaben an Gramm....
Die restlichen fünf Banderolen werde ich Ihnen schnellstens nachmailen.
Ich habe keine besonderen Wünsche, deshalb vertraue ich Ihren Designern und bin schon auf die ersten Vorschläge gespannt.

```html
<!DOCTYPE html>
<html lang="de">
<head>
<meta charset="utf-8">
<title>teigfein – Etikett Teigtaschen mit Käsefülle</title>
<link href="https://fonts.googleapis.com/css2?family=Cinzel:wght@400;600&family=Oswald:wght@300;400;500&display=swap" rel="stylesheet">
<style>
  :root {
    --bg-top: #8f8f8f;
    --bg-bottom: #dcdcdd;
    --label-black: #050505;
    --gold: #c9a351;
    --gold-light: #ecd08d;
    --gold-text: #d7b05a;
    --white: #ffffff;
    --ink: #2a1f17;
    --logo-green: #2f6a2b;
  }
  * { margin: 0; padding: 0; box-sizing: border-box; }
  html, body { width: 1172px; height: 1200px; overflow: hidden; }
  body {
    position: relative;
    background: linear-gradient(180deg, var(--bg-top) 0%, #b4b4b5 40%, var(--bg-bottom) 100%);
    font-family: "Oswald", sans-serif;
    font-weight: 300;
    color: var(--white);
  }
  .abs { position: absolute; }

  /* brand block */
  .brand-band {
    left: 444px; top: 55px; width: 292px; height: 31px;
    background: linear-gradient(90deg, var(--gold-light), var(--gold) 50%, var(--gold-light));
    display: flex; align-items: center; justify-content: center; gap: 14px;
  }
  .brand-band .rule { width: 28px; height: 1px; background: var(--white); }
  .brand-band span { font-size: 14px; letter-spacing: 5px; color: var(--white); white-space: nowrap; }
  .brand-mark { left: 444px; top: 95px; width: 60px; height: 60px; border-radius: 50%; background: var(--logo-green); }
  .brand-name { left: 516px; top: 96px; font-size: 38px; font-weight: 400; line-height: 1; }
  .brand-tagline { left: 532px; top: 140px; font-size: 16px; letter-spacing: .5px; }

  /* label */
  .label { left: 91px; top: 455px; width: 1023px; height: 292px; background: var(--label-black); }
  .crop { width: 1px; height: 316px; top: 443px; background: #6b6b6b; }
  .gold-rule { height: 1px; background: var(--gold); }

  .photo-panel {
    left: 421px; top: 455px; width: 407px; height: 292px;
    background: radial-gradient(circle at 187px 151px, #e7cfac 0, #d8b98f 95px, #f1ede6 112px, #5e5a55 140px, #2c2824 200px, #141210 100%);
  }
  .cheese-photo {
    left: 528px; top: 631px; width: 157px; height: 50px;
    border-radius: 4px 4px 60px 60px / 4px 4px 40px 40px;
    background: linear-gradient(120deg, #e9e2cf, #c8b58e 45%, #f3efe4 70%, #8a7a5d);
  }

  .section-title { font-family: "Cinzel", serif; font-size: 13.5px; color: var(--gold-text); letter-spacing: .3px; }
  .body-text { font-size: 8.6px; line-height: 13.7px; color: var(--white); }
  .body-text strong { font-weight: 500; }
  .ingredients { left: 195px; top: 504px; width: 204px; }
  .ingredients .row { display: flex; }
  .ingredients .key { width: 44px; flex: none; white-space: nowrap; }
  .prep { left: 195px; top: 578px; width: 196px; text-align: justify; hyphens: auto; -webkit-hyphens: auto; }
  .storage-title { left: 195px; top: 684px; font-size: 8px; font-weight: 500; letter-spacing: 1px; }
  .storage { left: 195px; top: 697px; width: 200px; line-height: 13px; }

  .center-band {
    left: 559px; top: 469px; width: 92px; height: 9px;
    background: linear-gradient(90deg, var(--gold-light), var(--gold));
    font-size: 4.5px; letter-spacing: 1.6px; text-align: center; line-height: 9px; white-space: nowrap;
  }
  .center-mark { left: 560px; top: 483px; width: 18px; height: 18px; border-radius: 50%; background: var(--logo-green); }
  .center-name { left: 582px; top: 481px; font-size: 14px; font-weight: 400; line-height: 1; }
  .product-title {
    left: 521px; top: 523px; width: 174px; text-align: center;
    font-family: "Cinzel", serif; font-weight: 600; color: var(--ink); font-size: 29px; line-height: 23px;
  }
  .filling-tag {
    left: 563px; top: 580px; width: 90px; height: 16px;
    background: var(--white); border: 1px solid var(--gold);
    font-size: 8px; font-weight: 500; letter-spacing: 1.4px; color: var(--ink);
    text-align: center; line-height: 14px;
  }
  .product-desc {
    left: 523px; top: 603px; width: 170px; text-align: center;
    font-size: 7.4px; line-height: 9.4px; font-weight: 400; color: var(--ink);
  }

  .claims { left: 872px; top: 484px; width: 160px; text-align: center; font-size: 7.2px; line-height: 10.5px; font-weight: 500; }
  .claims-rule { left: 937px; top: 524px; width: 30px; height: 1px; background: var(--gold); }
  .small-head { font-size: 6.2px; font-weight: 500; letter-spacing: .9px; line-height: 8px; white-space: nowrap; }
  .nutrition-head { left: 884px; top: 535px; }
  .nutrition { left: 884px; top: 545px; font-size: 5.8px; border-collapse: collapse; border-spacing: 0; }
  .nutrition td { padding: 0; height: 9.4px; line-height: 9.4px; white-space: nowrap; }
  .nutrition td:first-child { width: 71px; }
  .maker-head { left: 884px; top: 620px; }
  .maker { left: 884px; top: 632px; font-size: 5.8px; line-height: 9.2px; white-space: nowrap; }
  .maker .web { font-weight: 500; letter-spacing: .8px; font-size: 6.2px; margin-top: 2px; }
  .content-head { left: 884px; top: 673px; }
  .content { left: 883px; top: 683px; color: var(--gold-text); font-weight: 500; font-size: 17px; line-height: 19px; white-space: nowrap; }
  .content .portions { font-weight: 300; }
  .content .weight { padding-left: 42px; }
</style>
</head>
<body>

  <div class="abs brand-band"><i class="rule"></i><span>GRETA WOLKENHUBER</span><i class="rule"></i></div>
  <div class="abs brand-mark"></div>
  <div class="abs brand-name">teigfein</div>
  <div class="abs brand-tagline">Teigtaschen handgemacht</div>

  <div class="abs label"></div>
  <div class="abs crop" style="left:158px"></div>
  <div class="abs crop" style="left:1048px"></div>

  <div class="abs photo-panel" role="img" aria-label="Foto: bemehlte runde Holzplatte auf dunklem Holztisch, umgeben von Weizenähren, Olivenöl, Ei, Nudelholz und Gewürzen"></div>
  <div class="abs cheese-photo" role="img" aria-label="Foto: verschiedene Käsesorten mit Walnuss auf einem Brett"></div>

  <div class="abs gold-rule" style="left:179px; top:474px; width:354px"></div>
  <div class="abs gold-rule" style="left:690px; top:474px; width:342px"></div>
  <div class="abs gold-rule" style="left:179px; top:737px; width:851px"></div>

  <div class="abs section-title" style="left:195px; top:486px">ZUTATEN</div>
  <div class="abs body-text ingredients">
    <div class="row"><span class="key">TEIG &nbsp; (50%):</span><span>Dinkelmehl, Hartweizengriess, Eier, Olivenöl</span></div>
    <div class="row"><span class="key">FÜLLE (50%):</span><span>Käsemischung (Greyerzer, Emmentaler, Ricotta, Parmesan), Basilikum, Pfeffer, Meersalz</span></div>
  </div>
  <div class="abs section-title" style="left:195px; top:558px">ZUBEREITUNG</div>
  <div class="abs body-text prep">Großen Topf mit <strong>Salzwasser</strong> zum Sieden bringen. Die gefrorenen Teigtaschen vorsichtig einlegen, Hitze reduzieren, behutsam mit dem Holzlöffel einige Male umrühren und max. <strong>8 Minuten</strong> auf kleiner Stufe leicht kochen lassen. Teigtaschen vorsichtig mit dem Holzlöffel aus dem Wasser nehmen und mit dem entsprechenden Guss anrichten.</div>
  <div class="abs storage-title">AUFBEWAHRUNGSHINWEIS</div>
  <div class="abs body-text storage">Im Tiefkühlfach *** bei -18° Celsius mindestens haltbar bis siehe Etikette auf der Rückseite.</div>

  <div class="abs center-band">GRETA WOLKENHUBER</div>
  <div class="abs center-mark"></div>
  <div class="abs center-name">teigfein</div>
  <h1 class="abs product-title">TEIG<br>TASCHEN</h1>
  <div class="abs filling-tag">MIT KÄSEFÜLLE</div>
  <p class="abs product-desc">Handgemachte Teigtaschen gefüllt mit einem Mix aus Greyerzer, Emmentaler, Ricotta und Parmesan</p>

  <div class="abs claims">Ohne Konservierungsstoffe<br>Ohne künstliche Aromen<br>Ohne Geschmacksverstärker</div>
  <div class="abs claims-rule"></div>
  <div class="abs small-head nutrition-head">DURCHSCHNITTLICHE NÄHRWERTE / 100g</div>
  <table class="abs nutrition">
    <tr><td>Brennwert/Energie</td><td>000 KJ/000 kcal</td></tr>
    <tr><td>Fett</td><td>00 g</td></tr>
    <tr><td>davon ges. Fettsäuren</td><td>00g</td></tr>
    <tr><td>Kohlenhydrate</td><td>00g</td></tr>
    <tr><td>Zucker</td><td>00g</td></tr>
    <tr><td>Eiweiss</td><td>00g</td></tr>
    <tr><td>Salz</td><td>00g</td></tr>
  </table>
  <div class="abs small-head maker-head">HERSTELLER</div>
  <div class="abs maker">
    Greta Wolkenhuber · Am Lindenhang 7 · AT-6850 Dornbirn<br>
    T: +43 (0) 660 48 27 15 90 · Mail: wolkenhuber@mailpost.at
    <div class="web">www.teigfein.at</div>
  </div>
  <div class="abs small-head content-head">INHALT</div>
  <div class="abs content">
    <div>21 STÜCK <span class="portions">(3-4 Portionen)</span></div>
    <div class="weight">630 g ℮</div>
  </div>

</body>
</html>
```